Flyer Designer for a Widow and Door Company - loooking for fresh design

We are looking for a flyer designed to advertise our business - we supply and install windows and doors - we are looking for a fresh looking flyer to distribute to drum up business - more information can be found at our website www.brightpanehouse.co.uk - We want a different approach than we currently have - making it vibrant and fresh - you can see the services on the website but its more the graphical design that we are looking for rather than content as the content from the website can be used for each service etc.

Target Market(s)

the general public

Colors

Designer to choose colors to be used in the design.

Requirements
Must have
• vibrant design and images

```html
<!DOCTYPE html>
<html lang="en">
<head>
<meta charset="utf-8">
<title>Bright Pane House – Flyer</title>
<link href="https://fonts.googleapis.com/css2?family=Oswald:wght@500;700&family=Open+Sans:wght@400;600;700&display=swap" rel="stylesheet">
<style>
  :root{
    --blue:#1e7fd0;
    --blue-dark:#1565ad;
    --blue-light:#3d9be6;
    --grey:#7d7f82;
    --grey-light:#b7b9bb;
    --ink:#333a40;
    --white:#ffffff;
    --mat:#b9c4c8;
  }
  *{margin:0;padding:0;box-sizing:border-box}
  html,body{width:1200px;height:2400px;overflow:hidden;background:var(--mat)}
  .canvas{position:relative;width:1200px;height:2400px}
  .flyer{position:absolute;left:30px;top:394px;width:1140px;height:1612px;background:var(--white);overflow:hidden;box-shadow:0 4px 18px rgba(0,0,0,.18)}
  .hero-photo{position:absolute;left:0;top:0;width:1140px;height:1000px;
    background:linear-gradient(180deg,#8a9096 0%,#6f777e 40%,#9aa0a5 70%,#c9cbcc 100%)}
  .shapes{position:absolute;left:0;top:0;width:1140px;height:1612px}
  .brand{position:absolute;left:370px;top:40px;width:400px;display:flex;align-items:center;justify-content:center;gap:14px}
  .brand-mark{width:46px;height:46px;background:var(--blue)}
  .brand-name{font-family:'Oswald',sans-serif;font-weight:700;font-size:34px;line-height:1;color:var(--blue);letter-spacing:1px}
  .call{position:absolute;left:0;width:1140px;text-align:center;font-family:'Oswald',sans-serif;font-weight:700;color:var(--white);transform:skewX(-10deg)}
  .call-label{top:430px;font-size:66px}
  .call-number{top:510px;font-size:82px;letter-spacing:2px}
  .headline{position:absolute;left:410px;top:748px;width:360px;text-align:center;font-family:'Oswald',sans-serif;font-weight:700;font-size:44px;line-height:1.15;color:var(--white);text-transform:uppercase}
  .services-title{position:absolute;left:130px;top:1050px;font-family:'Oswald',sans-serif;font-weight:500;font-size:46px;color:var(--blue)}
  .service{position:absolute;width:390px;display:flex;gap:22px;align-items:flex-start}
  .service-icon{flex:none;width:88px;height:88px}
  .service h3{font-family:'Oswald',sans-serif;font-weight:500;font-size:20px;color:var(--blue);text-transform:uppercase;margin:6px 0 4px}
  .service p{font-family:'Open Sans',sans-serif;font-size:17px;line-height:1.35;color:var(--ink)}
  .service-windows{left:130px;top:1140px}
  .service-doors{left:130px;top:1300px}
  .service-repairs{left:680px;top:1140px}
  .service-landlord{left:680px;top:1300px}
  .footer-address{position:absolute;left:60px;top:1462px;display:flex;gap:12px;align-items:flex-start;font-family:'Open Sans',sans-serif;font-weight:600;font-size:17px;line-height:1.4;color:var(--white)}
  .footer-web{position:absolute;left:640px;top:1478px;display:flex;gap:12px;align-items:center;font-family:'Open Sans',sans-serif;font-weight:600;font-size:18px;color:var(--white)}
  .social{position:absolute;left:960px;top:1468px;display:flex;gap:12px}
  .social span{width:44px;height:44px;border:3px solid var(--white);border-radius:50%}
</style>
</head>
<body>
<div class="canvas">
  <div class="flyer">
    <div class="hero-photo" role="img" aria-label="Photo of a grey clapboard house with white dormer windows and a yellow front door"></div>

    <svg class="shapes" viewBox="0 0 1140 1612" xmlns="http://www.w3.org/2000/svg">
      <defs>
        <linearGradient id="doorDark" x1="0" y1="0" x2="1" y2="1">
          <stop offset="0" stop-color="#5a5f66"/><stop offset="1" stop-color="#2c3036"/>
        </linearGradient>
        <linearGradient id="doorsPair" x1="0" y1="0" x2="1" y2="1">
          <stop offset="0" stop-color="#8a4a3a"/><stop offset=".5" stop-color="#3a3d42"/><stop offset="1" stop-color="#1f2226"/>
        </linearGradient>
      </defs>
      <!-- white lower field with V cut -->
      <polygon points="0,560 600,1160 1140,620 1140,1612 0,1612" fill="var(--white)"/>
      <!-- top logo triangle with blue wedges -->
      <polygon points="250,0 330,0 570,240 570,300" fill="var(--blue)"/>
      <polygon points="890,0 810,0 570,240 570,300" fill="var(--blue)"/>
      <polygon points="330,0 810,0 570,240" fill="var(--white)"/>
      <!-- side accents -->
      <polygon points="0,330 130,450 0,570" fill="var(--blue)"/>
      <polygon points="1140,400 1040,500 1140,600" fill="var(--blue)"/>
      <!-- left door photo diamond -->
      <g role="img" aria-label="Photo of a dark grey composite front door">
        <polygon points="210,620 390,800 210,980 30,800" fill="url(#doorDark)"/>
      </g>
      <!-- right doors photo diamond -->
      <g role="img" aria-label="Photos of a red door and a black composite door">
        <polygon points="960,560 1150,750 960,940 770,750" fill="url(#doorsPair)"/>
      </g>
      <!-- small squares -->
      <rect x="300" y="610" width="60" height="60" fill="var(--blue)"/>
      <rect x="370" y="650" width="40" height="40" fill="var(--grey)"/>
      <rect x="820" y="560" width="70" height="70" fill="var(--grey)"/>
      <rect x="770" y="520" width="40" height="40" fill="var(--blue)"/>
      <rect x="860" y="930" width="80" height="80" fill="var(--grey)"/>
      <rect x="950" y="960" width="44" height="44" fill="var(--grey-light)"/>
      <rect x="260" y="960" width="40" height="40" fill="var(--blue)"/>
      <!-- blue headline diamond -->
      <polygon points="590,600 870,880 590,1160 310,880" fill="var(--white)"/>
      <polygon points="590,620 850,880 590,1140 330,880" fill="var(--blue)"/>
      <!-- footer -->
      <rect x="0" y="1440" width="1140" height="110" fill="var(--blue)"/>
      <polygon points="0,1440 560,1440 520,1550 0,1550" fill="var(--blue-dark)"/>
      <rect x="0" y="1550" width="1140" height="62" fill="var(--white)"/>
      <rect x="0" y="1590" width="1140" height="22" fill="var(--blue-light)"/>
    </svg>

    <div class="brand"><span class="brand-mark"></span><span class="brand-name">BRIGHT PANE HOUSE LTD</span></div>

    <div class="call call-label">Call Us Today</div>
    <div class="call call-number">01632 960415</div>

    <h1 class="headline">Installers &amp; Suppliers of Bespoke Windows &amp; Doors</h1>

    <h2 class="services-title">Our Services</h2>

    <div class="service service-windows">
      <svg class="service-icon" viewBox="0 0 88 88"><circle cx="44" cy="44" r="40" fill="none" stroke="var(--blue)" stroke-width="4"/><rect x="28" y="24" width="32" height="40" fill="none" stroke="var(--blue)" stroke-width="4"/><line x1="44" y1="24" x2="44" y2="64" stroke="var(--blue)" stroke-width="3"/><line x1="28" y1="44" x2="60" y2="44" stroke="var(--blue)" stroke-width="3"/></svg>
      <div><h3>Our Windows</h3><p>Our windows are individually designed to suit your home, bespoke to your individual requirements.</p></div>
    </div>
    <div class="service service-doors">
      <svg class="service-icon" viewBox="0 0 88 88"><circle cx="44" cy="44" r="40" fill="none" stroke="var(--blue)" stroke-width="4"/><rect x="30" y="22" width="28" height="44" fill="var(--blue)"/><circle cx="52" cy="46" r="2.5" fill="var(--white)"/></svg>
      <div><h3>Our Doors</h3><p>A new door from Bright Pane House can transform the look of your home, offer increased security.</p></div>
    </div>
    <div class="service service-repairs">
      <svg class="service-icon" viewBox="0 0 88 88"><circle cx="44" cy="44" r="40" fill="var(--white)"/><line x1="26" y1="26" x2="62" y2="62" stroke="var(--blue)" stroke-width="7" stroke-linecap="round"/><line x1="62" y1="26" x2="26" y2="62" stroke="var(--ink)" stroke-width="7" stroke-linecap="round"/></svg>
      <div><h3>Repairs</h3><p>At Bright Pane House we offer a full repair and replacement service on glass units, windows and doors.</p></div>
    </div>
    <div class="service service-landlord">
      <svg class="service-icon" viewBox="0 0 88 88"><circle cx="44" cy="44" r="40" fill="var(--blue)"/><path d="M24 30h40v22H40l-10 8v-8h-6z" fill="var(--white)"/></svg>
      <div><h3>Landlord Services</h3><p>We work closely with Landlords &amp; Letting Agents to offer a full repair or replacement service on</p></div>
    </div>

    <div class="footer-address">
      <svg width="22" height="30" viewBox="0 0 22 30"><path d="M11 0C5 0 0 5 0 11c0 8 11 19 11 19s11-11 11-19C22 5 17 0 11 0z" fill="var(--white)"/><circle cx="11" cy="11" r="4" fill="var(--blue-dark)"/></svg>
      <div>Millbrook House, Canal Lane<br>Ashford Vale, Northshire, AV4 2LT</div>
    </div>
    <div class="footer-web">
      <svg width="24" height="24" viewBox="0 0 24 24"><circle cx="12" cy="12" r="10" fill="none" stroke="var(--white)" stroke-width="2"/><line x1="2" y1="12" x2="22" y2="12" stroke="var(--white)" stroke-width="2"/><ellipse cx="12" cy="12" rx="4" ry="10" fill="none" stroke="var(--white)" stroke-width="2"/></svg>
      <span>www.brightpanehouse.co.uk</span>
    </div>
    <div class="social"><span></span><span></span><span></span></div>
  </div>
</div>
</body>
</html>
```